GLS biz card

We need a business card design for our new company based in Los Angeles called "Gold Lantern Studios". We develop film and television projects. We work with investors, financiers, film production companies, film distribution and sales companies as well as studios. We would like to incorporate our logo (see attached) on a two-sided card. We need to include: name and title, address, phone, email and company website.

Target Market(s)

Business, financial and studio clients

Industry/Entity Type

Business

Contact Information for Business Card

Two-sided. We are thinking of the logo on one side and the information on the back. Please feel free to be creative! Thanks.

Requirements
Must have
• Please include the following text information, excluding the "CAPS CATEGORY:" and please allow the ability for us to change the name, title and email address for each company employee):
• NAME & TITLE:
• Peter Dunmore
• Managing Partner
• COMPANY NAME:
• GOLD LANTERN STUDIOS (please use existing logo)
• COMPANY ADDRESS:
• KVT Arts Park
• 2480 Wexley Boulevard
• Arts Hall, 4th Floor
• Manhattan Beach, CA 90266
• COMPANY PHONE NUMBER:
• 310-555-4206
• COMPANY WEBSITE ADDRESS:
• www.goldlanternstudioshouse.com
• EMAIL ADDRESS: (only one per card)
• frank@goldlanternstudioshouse.com
• tizzy@goldlanternstudioshouse.com
• peter@goldlanternstudioshouse.com

```html
<!DOCTYPE html>
<html lang="en">
<head>
<meta charset="utf-8">
<title>Gold Lantern Studios – Business Card</title>
<link rel="stylesheet" href="https://fonts.googleapis.com/css2?family=Open+Sans:wght@400;600&family=Michroma&display=swap">
<style>
  :root {
    --page: #e9e7e3;
    --teal-deep: #0a3844;
    --teal-mid: #0f5d72;
    --teal-bright: #1fb3df;
    --cyan-glow: #33c8f2;
    --black: #050607;
    --charcoal: #15191c;
    --white: #ffffff;
    --muted: #b9d3dc;
  }
  * { box-sizing: border-box; margin: 0; padding: 0; }
  html, body {
    width: 1200px; height: 784px; overflow: hidden;
    background: var(--page);
  }
  .sheet {
    width: 1200px; height: 784px;
    display: flex; align-items: center; justify-content: center; gap: 40px;
  }
  .card {
    position: relative; width: 560px; height: 320px; overflow: hidden;
    border-radius: 4px;
    box-shadow: 0 6px 18px rgba(0,0,0,.25);
  }

  /* Contact side */
  .card--info {
    background: linear-gradient(100deg, var(--teal-deep) 0%, var(--teal-mid) 45%, var(--teal-bright) 100%);
    font-family: "Open Sans", sans-serif; color: var(--white);
  }
  .card__pattern {
    position: absolute; right: 0; top: 0; width: 66%; height: 100%;
    background: radial-gradient(ellipse at 85% 40%, rgba(80,210,245,.55), rgba(31,179,223,.15) 60%, transparent 80%);
  }
  .brand {
    position: absolute; display: flex; flex-direction: column; align-items: center;
  }
  .brand__dot { border-radius: 50%; background: var(--cyan-glow); }
  .brand__name {
    font-family: "Michroma", sans-serif; color: var(--cyan-glow);
    letter-spacing: .06em; white-space: nowrap;
  }
  .brand__tag {
    font-family: "Open Sans", sans-serif; color: var(--muted);
    letter-spacing: .18em; text-transform: uppercase; white-space: nowrap;
  }
  .card--info .brand { left: 28px; top: 40px; }
  .card--info .brand__dot { width: 34px; height: 34px; margin-bottom: 10px; }
  .card--info .brand__name { font-size: 13px; }
  .card--info .brand__tag { font-size: 6px; margin-top: 4px; }

  .person { position: absolute; right: 26px; top: 18px; text-align: right; }
  .person__name { font-size: 16px; font-weight: 400; }
  .person__title { font-size: 9px; color: var(--muted); margin-top: 1px; }

  .contacts {
    position: absolute; left: 26px; bottom: 20px; list-style: none;
    font-size: 14px; line-height: 21px;
  }
  .contacts li { display: flex; align-items: center; gap: 8px; white-space: nowrap; }
  .contacts svg { width: 13px; height: 13px; fill: var(--white); flex: none; }
  .contacts__cont { padding-left: 21px; }

  /* Logo side */
  .card--logo {
    background: radial-gradient(circle at 58% 40%, var(--charcoal) 0%, var(--black) 65%);
  }
  .card__ring {
    position: absolute; left: -40px; top: 20px; width: 340px; height: 340px;
    border-radius: 50%;
    background: radial-gradient(circle, transparent 58%, rgba(255,255,255,.05) 60%, transparent 64%);
  }
  .card--logo .brand { left: 50%; top: 48px; transform: translateX(-50%); margin-left: 40px; }
  .card--logo .brand__dot {
    width: 96px; height: 96px; margin-bottom: 18px;
    box-shadow: 0 0 40px rgba(51,200,242,.45);
  }
  .card--logo .brand__name { font-size: 18px; }
  .card--logo .brand__tag { font-size: 8px; margin-top: 10px; color: var(--white); }
</style>
</head>
<body>
<main class="sheet">

  <section class="card card--info" aria-label="Business card, contact side">
    <div class="card__pattern" role="img" aria-label="Decorative pattern of teal ovals receding in perspective"></div>

    <div class="brand">
      <span class="brand__dot"></span>
      <span class="brand__name">GOLD LANTERN STUDIOS</span>
      <span class="brand__tag">A Media Entertainment Company</span>
    </div>

    <div class="person">
      <p class="person__name">Peter Dunmore</p>
      <p class="person__title">Managing Partner</p>
    </div>

    <ul class="contacts">
      <li>
        <svg viewBox="0 0 16 16" aria-hidden="true"><path d="M3 1l3 3-1.5 2a9 9 0 0 0 5.5 5.5L12 10l3 3-2 2C7 15 1 9 1 3z"/></svg>
        310-555-4206
      </li>
      <li>
        <svg viewBox="0 0 16 16" aria-hidden="true"><path d="M8 1a7 7 0 1 0 0 14A7 7 0 0 0 8 1zm0 1.5c.8 0 1.8 1.6 2.1 4.5H5.9C6.2 4.1 7.2 2.5 8 2.5zM2.6 7h1.8a12 12 0 0 1 .6-3.6A5.5 5.5 0 0 0 2.6 7zm0 2a5.5 5.5 0 0 0 2.4 3.6A12 12 0 0 1 4.4 9zm3.3 0h4.2c-.3 2.9-1.3 4.5-2.1 4.5S6.2 11.9 5.9 9zm5.7 0a12 12 0 0 1-.6 3.6A5.5 5.5 0 0 0 13.4 9zm1.8-2A5.5 5.5 0 0 0 11 3.4 12 12 0 0 1 11.6 7z"/></svg>
        www.goldlanternstudioshouse.com
      </li>
      <li>
        <svg viewBox="0 0 16 16" aria-hidden="true"><path d="M1 3h14v10H1zm1.5 1.5v.3L8 9l5.5-4.2v-.3z"/></svg>
        peter@goldlanternstudioshouse.com
      </li>
      <li>
        <svg viewBox="0 0 16 16" aria-hidden="true"><path d="M8 1l7 6h-2v8H10v-5H6v5H3V7H1z"/></svg>
        KVT Arts Park, 2480 Wexley Boulevard
      </li>
      <li class="contacts__cont">Arts Hall, 4th Floor, Manhattan Beach, CA 90266</li>
    </ul>
  </section>

  <section class="card card--logo" aria-label="Business card, logo side">
    <div class="card__ring"></div>
    <div class="brand">
      <span class="brand__dot"></span>
      <span class="brand__name">GOLD LANTERN STUDIOS</span>
      <span class="brand__tag">A Media Entertainment Company</span>
    </div>
  </section>

</main>
</body>
</html>
```